Cover for Where the Quiet River Bends Beyond Our Morning

Cover for a book that describes everything that happens to a person, from pre-birth life plans through growing in compassion and wisdom to death and living in the afterlife. The information is revealed in messages from people living in the life after this life. The title is Lanterns Along the Hidden Stair of Every Soul: Gathered from Voices Dwelling in the Further Meadow. Author is T. Morven Ashdale. Book size is 6 by 9.

Target Market(s)

General

Font styles to use
Serif

```html
<!DOCTYPE html>
<html lang="en">
<head>
<meta charset="utf-8">
<title>Lanterns Along the Hidden Stair of Every Soul — Book Cover</title>
<link rel="stylesheet" href="https://fonts.googleapis.com/css2?family=Marcellus&display=swap">
<style>
  :root {
    --teal-deep: #142429;
    --teal-mid: #23393d;
    --stone-grey: #3e4a4b;
    --ember: #8a5a3c;
    --warm-glow: #c99a6e;
    --earth: #2b1f19;
    --earth-deep: #161110;
    --title-white: #ffffff;
    --subtitle-white: #f1ede8;
    --author-red: #d8292b;
  }
  html, body {
    margin: 0;
    padding: 0;
    width: 800px;
    height: 1200px;
    overflow: hidden;
    background: #ffffff;
  }
  .cover {
    position: relative;
    width: 800px;
    height: 1200px;
    overflow: hidden;
    font-family: "Marcellus", serif;
    background: var(--teal-deep);
  }
  .cover-art {
    position: absolute;
    inset: 0;
    background: linear-gradient(180deg,
      var(--teal-deep) 0%,
      var(--teal-mid) 30%,
      var(--stone-grey) 50%,
      var(--ember) 64%,
      var(--warm-glow) 72%,
      var(--ember) 80%,
      var(--earth) 90%,
      var(--earth-deep) 100%);
  }
  .title {
    position: absolute;
    inset: 0;
    margin: 0;
    font-weight: 400;
    color: var(--title-white);
    text-shadow: 0 2px 6px rgba(0, 0, 0, 0.4);
  }
  .title-line {
    position: absolute;
    left: 0;
    right: 0;
    text-align: center;
    font-size: 68px;
    line-height: 1;
    letter-spacing: 4px;
    white-space: nowrap;
  }
  .subtitle {
    position: absolute;
    left: 0;
    right: 0;
    top: 617px;
    margin: 0;
    text-align: center;
    font-size: 33px;
    line-height: 45px;
    letter-spacing: 2px;
    font-weight: 400;
    color: var(--subtitle-white);
    text-shadow: 0 2px 5px rgba(0, 0, 0, 0.45);
  }
  .author {
    position: absolute;
    left: 0;
    right: 0;
    top: 1103px;
    margin: 0;
    text-align: center;
    font-size: 58px;
    line-height: 1;
    letter-spacing: 3px;
    font-weight: 400;
    color: var(--author-red);
  }
</style>
</head>
<body>
  <main class="cover">
    <div class="cover-art" role="img" aria-label="Photograph of an open stone tomb: a round stone rolled aside, warm light glowing from the entrance and folded linen cloth on the ground"></div>

    <h1 class="title">
      <span class="title-line" style="top:47px;">Lanterns Along</span>
      <span class="title-line" style="top:138px;">the Hidden</span>
      <span class="title-line" style="top:232px;">Stair</span>
      <span class="title-line" style="top:325px;">of</span>
      <span class="title-line" style="top:405px;">Every</span>
      <span class="title-line" style="top:499px;">Soul</span>
    </h1>

    <p class="subtitle">Gathered from Voices Dwelling<br>in the Further Meadow</p>

    <p class="author">T. Morven Ashdale</p>
  </main>
</body>
</html>
```